Games company needs intuitive redesign for lottery engagement game.

We require the interface of our lottery prediction game to be redesigned not just cosmetically but functionally also. In this game, users are presented with a series of questions relating to the upcoming lottery draw and have to make a binary choice if they think the statement on the card is true or false (Y/N). This prediction dynamic forms the crux of our game and should be maintained but colours, branding and method of interaction are all free to be changed Designers should note that the red text boxes on the briefing screens would not be present in the final product and are only there to clarify app functionality. App screens progress chronologically from 1-12 Any further questions or queries that would aid design works please message directly.

```html
<!DOCTYPE html>
<html lang="en">
<head>
<meta charset="utf-8">
<title>Prediction Card</title>
<link rel="stylesheet" href="https://fonts.googleapis.com/css2?family=Poppins:wght@300;600;700&display=swap">
<style>
  :root {
    --pink: #f76f8e;
    --bg-rose: #c07080;
    --bg-rose-light: #c98a98;
    --bg-grey: #c4c4c4;
    --navy: #2e2f4a;
    --ink: #4a3f47;
    --white: #ffffff;
    --track: #9a9a9a;
    --green: #9aad72;
  }
  html, body {
    margin: 0; padding: 0;
    width: 1200px; height: 2403px; overflow: hidden;
    font-family: "Poppins", sans-serif;
  }
  .screen { position: relative; width: 1200px; height: 2403px; overflow: hidden;
    background: linear-gradient(to bottom, var(--bg-rose) 0, var(--bg-rose) 1040px, var(--bg-grey) 1120px, var(--bg-grey) 2060px, var(--navy) 2120px); }
  .blur { position: absolute; filter: blur(14px); border-radius: 30px; }
  .blur.bar-a { left: 260px; top: 120px; width: 310px; height: 60px; background: var(--bg-rose-light); }
  .blur.bar-b { left: 140px; top: 330px; width: 900px; height: 50px; background: var(--bg-rose-light); }
  .blur.bar-c { left: 90px; top: 430px; width: 150px; height: 70px; background: var(--bg-rose-light); }
  .blur.bar-d { left: 270px; top: 450px; width: 700px; height: 60px; background: #b06272; }
  .blur.side { left: 60px; top: 1080px; width: 40px; height: 420px; background: var(--green); }
  .blur.glow { left: 340px; top: 2180px; width: 520px; height: 160px; background: #8a5a8e; border-radius: 80px; filter: blur(30px); }
  .cta-blur { position: absolute; left: 365px; top: 1898px; width: 460px; height: 131px; border-radius: 66px; background: var(--green); filter: blur(10px); }

  .card { position: absolute; width: 1031px; height: 1169px; border-radius: 58px; overflow: hidden;
    background: var(--white); box-shadow: 0 20px 50px rgba(0,0,0,0.18); }
  .card.back { left: 85px; top: 572px; }
  .card .date { position: absolute; left: 163px; top: 640px; margin: 0; }
  .date { color: var(--pink); font-weight: 700; font-size: 67px; line-height: 1; }
  .card.back .date { left: 163px; top: 80px; }
  .card.back .question { position: absolute; left: 83px; top: 710px; margin: 0; width: 860px;
    color: var(--ink); font-weight: 300; font-size: 56px; line-height: 85px; }
  .action-bar { position: absolute; left: 0; bottom: 0; width: 100%; height: 168px; background: var(--pink);
    color: var(--white); font-weight: 600; font-size: 50px; }
  .action-bar .no { position: absolute; left: 75px; top: 50%; transform: translateY(-50%); display: flex; align-items: center; gap: 14px; }
  .action-bar .swipe { position: absolute; left: 515px; top: 50%; transform: translate(-50%, -50%); }

  .card.front { left: 344px; top: 468px; height: 1148px; transform: rotate(30deg); }
  .card.front .header { position: absolute; left: 0; top: 0; width: 100%; height: 616px; background: var(--pink); }
  .card.front .answer { position: absolute; left: 488px; top: 305px; transform: translate(-50%, -50%);
    color: var(--white); font-weight: 700; font-size: 170px; letter-spacing: 4px; line-height: 1; }
  .card.front .question { position: absolute; left: 80px; top: 770px; margin: 0; width: 880px;
    color: var(--ink); font-weight: 300; font-size: 58px; line-height: 85px; }

  .progress { position: absolute; left: 248px; top: 1796px; display: flex; gap: 26px; }
  .progress span { width: 120px; height: 14px; background: var(--track); }
  .progress span.active { background: var(--white); }
</style>
</head>
<body>
<div class="screen">
  <div class="blur bar-a"></div>
  <div class="blur bar-b"></div>
  <div class="blur bar-c"></div>
  <div class="blur bar-d"></div>
  <div class="blur side"></div>
  <div class="cta-blur"></div>
  <div class="blur glow"></div>

  <div class="card back">
    <p class="date">Wed 21</p>
    <p class="question">Will there be more EVEN than ODD numbers in tonight's Emerald Lotto?</p>
    <div class="action-bar">
      <span class="no">
        <svg width="52" height="46" viewBox="0 0 52 46" aria-hidden="true"><path d="M50 23H6M24 4L5 23l19 19" fill="none" stroke="#fff" stroke-width="6" stroke-linecap="round" stroke-linejoin="round"/></svg>
        NO
      </span>
      <span class="swipe">SWIPE</span>
    </div>
  </div>

  <div class="card front">
    <div class="header"><span class="answer">YES</span></div>
    <p class="question">Will there be more EVEN than ODD numbers in tonight's Emerald Lotto?</p>
  </div>

  <div class="progress">
    <span class="active"></span><span></span><span></span><span></span><span></span>
  </div>
</div>
</body>
</html>
```